Business Card and Logo Color Scheme Design Contest

We are starting a new company called Lone Ridge Structural Partners and already have a logo however, the colors for the logo itself are not final and COULD be changed. I'm hoping to move AWAYfrom the gold color in the card and the logo as it seems a bit outdated. What we need help with is to find what our business color scheme will be, and then incorporate those colors into both the logo and the business card design itself. We also want to make sure we are known as "LRS" so in the future we can just refer to ourselves as "LRS" and not Lone Ridge Structural Partners. That being said, I would like to make a slight change to the logo to somehow include the letters "LRS." The logo used in the front of the card design MUST ALSO include the words "Firm No. 64307" within the logo. My vision is for the front of the card to have the information shown in the attached image. For the back of the card, I'm hoping to have something very simple. I'm envisioning a solid color with either the website (www.bridgemarkplans.com) and a simplified version of the logo. I've attached an example but I'm looking for a complete redesign. I'm looking for a slick, modern and simple design.

Industry/Entity Type

Civil Engineer

Contact Information for Business Card

Logo
Firm No. 64307
Marcus Holloway, PE
Chief Operating Officer
Email:mholloway@bridgemarkplans.com
Ph: 555.201.0142 | D: 555.201.0178 | M:555.304.0263
4187 W. Kellingham, Harlow Springs, Colorado 80917
www.bridgemarkplans.com

Requirements
Must have
• Logo
Contact Info
Nice to have
• "LRS" Incorporated in the design
Should not have
• The current color scheme

```html
<!DOCTYPE html>
<html lang="en">
<head>
<meta charset="utf-8">
<title>Lone Ridge Structural Partners — Business Card</title>
<link rel="stylesheet" href="https://fonts.googleapis.com/css2?family=Barlow:wght@400;600;700&display=swap">
<style>
  :root {
    --backdrop: #1c2b7a;
    --card: #ffffff;
    --card-front: #f9f9f9;
    --ink: #1a2040;
    --band: #1b2340;
    --band-text: #ffffff;
  }
  * { box-sizing: border-box; margin: 0; padding: 0; }
  html, body {
    width: 1200px;
    height: 1200px;
    overflow: hidden;
    background: var(--backdrop);
    font-family: "Barlow", sans-serif;
    color: var(--ink);
  }
  .stage { position: relative; width: 1200px; height: 1200px; }

  .card {
    position: absolute;
    left: 286px;
    width: 634px;
    height: 362px;
    background: var(--card);
  }
  .card--front { top: 202px; background: var(--card-front); }
  .card--back { top: 620px; }

  .wordmark {
    position: absolute;
    left: 0; right: 0;
    top: 118px;
    text-align: center;
    font-weight: 700;
    color: var(--ink);
    text-transform: uppercase;
  }
  .wordmark__initials {
    display: block;
    font-size: 60px;
    line-height: 50px;
    letter-spacing: 8px;
    padding-left: 8px;
  }
  .wordmark__name {
    display: block;
    margin-top: 14px;
    font-size: 23px;
    line-height: 23px;
    letter-spacing: 0.8px;
  }
  .wordmark__firm {
    display: block;
    margin-top: 3px;
    font-size: 11px;
    letter-spacing: 0.4px;
  }

  .person {
    position: absolute;
    left: 0; right: 0;
    top: 88px;
    text-align: center;
  }
  .person__name {
    font-size: 23px;
    font-weight: 700;
    line-height: 26px;
    letter-spacing: 0.3px;
  }
  .person__title {
    font-size: 20px;
    font-weight: 400;
    line-height: 22px;
    letter-spacing: 0.6px;
  }

  .contact {
    position: absolute;
    top: 210px;
    font-size: 16.5px;
    line-height: 21.5px;
    letter-spacing: 0.2px;
  }
  .contact--phones { left: 37px; }
  .contact--phones b { font-weight: 700; }
  .contact--phones .label { display: inline-block; width: 30px; }
  .contact--address { right: 39px; text-align: right; }
  .contact__icon { width: 12px; height: 12px; vertical-align: -1px; margin-left: 4px; }

  .band {
    position: absolute;
    left: 0; right: 0;
    top: 299px;
    height: 42px;
    background: var(--band);
    color: var(--band-text);
    display: flex;
    align-items: center;
    justify-content: flex-end;
    padding-right: 39px;
    font-size: 19px;
    letter-spacing: 0.6px;
  }
  .band__icon { width: 12px; height: 12px; margin-left: 6px; }
</style>
</head>
<body>
<main class="stage">

  <section class="card card--front" aria-label="Card front">
    <div class="wordmark">
      <span class="wordmark__initials">LRS</span>
      <span class="wordmark__name">Lone Ridge Structural<br>Partners, LLC</span>
      <span class="wordmark__firm">Firm No. 64307</span>
    </div>
  </section>

  <section class="card card--back" aria-label="Card back">
    <div class="person">
      <p class="person__name">MARCUS HOLLOWAY, PE</p>
      <p class="person__title">Chief Operating Officer</p>
    </div>

    <div class="contact contact--phones">
      <p><span class="label">Ph:</span><b>555.201.0142</b></p>
      <p><span class="label">D :</span><b>555.201.0178</b></p>
      <p><span class="label">M :</span><b>555.304.0263</b></p>
    </div>

    <div class="contact contact--address">
      <p>4187 W. Kellingham</p>
      <p>Harlow Springs, Colorado 80917</p>
      <p>mholloway@bridgemarkplans.com<svg class="contact__icon" viewBox="0 0 12 12" aria-hidden="true"><rect x="0.75" y="2.25" width="10.5" height="7.5" rx="1" fill="none" stroke="currentColor" stroke-width="1.3"/><path d="M1 3 L6 7 L11 3" fill="none" stroke="currentColor" stroke-width="1.3"/></svg></p>
    </div>

    <div class="band">
      <span>www.bridgemarkplans.com</span>
      <svg class="band__icon" viewBox="0 0 12 12" aria-hidden="true"><circle cx="6" cy="6" r="5.5" fill="#ffffff"/><path d="M3 4.5 Q5 3 6 5 T9 6.5 M4 8 Q6 7 8 9" fill="none" stroke="var(--band)" stroke-width="1.3"/></svg>
    </div>
  </section>

</main>
</body>
</html>
```